Hi everyone,
Bright Nest Homes is a business that renovates older houses into modern homes. I'm looking for a design that is clean and simple. It needs to show the client that renovating is a simple process. No more than 3 colours to be used thanks.

What I need:
1. Logo
2. Business card (one side)
3. Letter head (A4)

Looking forward to the designs!

Industry/Entity Type

Construction

Logo Text

Bright Nest Homes

Font styles to use
Sans Serif

Requirements
Must have
• Trading name: Bright Nest Homes
• Contact name: Declan Ferris
• Email: declanferris@brightnesthomes.com.au
• Tel: 0417 582 046
• Clean and simple
Nice to have
• If design might include a few tools. eg Hammer, paint roller etc.
Should not have
• Complicated design

```html
<!DOCTYPE html>
<html lang="en">
<head>
<meta charset="utf-8">
<title>Bright Nest Homes — Stationery</title>
<link rel="stylesheet" href="https://fonts.googleapis.com/css2?family=Open+Sans:wght@400;600;700;800&display=swap">
<style>
  :root {
    --navy: #1b3a5c;
    --orange: #f47b20;
    --ink: #3c4650;
    --paper: #ffffff;
    --backdrop: #eeeeee;
    --font: "Open Sans", Arial, sans-serif;
  }
  * { box-sizing: border-box; margin: 0; padding: 0; }
  html, body { width: 1200px; height: 795px; overflow: hidden; }
  body { background: var(--backdrop); font-family: var(--font); color: var(--ink); position: relative; }

  /* Brand lock-up: plain square + name */
  .brand { display: flex; align-items: center; gap: 6px; color: var(--navy); font-weight: 800; white-space: nowrap; }
  .brand__mark { background: var(--orange); flex: none; border-radius: 2px; }
  .brand--sm { font-size: 14px; }
  .brand--sm .brand__mark { width: 14px; height: 14px; }
  .brand--md { font-size: 20px; gap: 8px; }
  .brand--md .brand__mark { width: 20px; height: 20px; }
  .brand--lg { font-size: 40px; gap: 14px; }
  .brand--lg .brand__mark { width: 42px; height: 42px; border-radius: 4px; }

  /* Letterhead */
  .letterhead {
    position: absolute; left: 70px; top: 45px; width: 495px; height: 700px;
    background: var(--paper); box-shadow: 0 2px 10px rgba(0,0,0,.08);
    padding: 40px 44px 0;
  }
  .letterhead__head { display: flex; justify-content: center; }
  .letterhead__date { text-align: right; font-size: 7px; font-weight: 700; color: var(--navy); margin-top: 10px; }
  .recipient { margin-top: 40px; font-size: 7.5px; font-weight: 700; color: var(--navy); line-height: 1.45; }
  .letter { margin-top: 34px; font-size: 7.2px; line-height: 1.6; }
  .letter__salutation { font-weight: 700; color: var(--navy); margin-bottom: 10px; }
  .letter p { margin-bottom: 10px; text-align: justify; }
  .letter__closing { font-weight: 700; color: var(--navy); }
  .signoff { position: absolute; right: 48px; top: 470px; width: 110px; font-size: 7px; }
  .signoff__name { font-weight: 700; color: var(--navy); }
  .signoff__role { color: var(--ink); }
  .signoff__signature { display: block; margin-top: 4px; width: 90px; height: 26px; background: linear-gradient(90deg, #e3e9f0, #f4f6f9); border-radius: 2px; }
  .letterhead__foot { position: absolute; left: 30px; right: 30px; bottom: 28px; border-top: 1px solid var(--navy); padding-top: 6px; text-align: center; }
  .foot__name { font-size: 7.5px; font-weight: 700; color: var(--orange); letter-spacing: .5px; }
  .foot__contact { font-size: 6.4px; color: var(--navy); margin-top: 3px; white-space: nowrap; }
  .foot__contact b { font-weight: 700; }

  /* Showcase logo */
  .logo-showcase { position: absolute; left: 625px; top: 80px; }

  /* Business cards */
  .card { position: absolute; width: 340px; height: 195px; background: var(--paper); box-shadow: 0 2px 10px rgba(0,0,0,.08); }
  .card--back { left: 790px; top: 215px; width: 340px; display: flex; align-items: center; justify-content: center; }
  .card--front { left: 640px; top: 460px; padding: 26px 28px; }
  .card__person { margin: 26px 0 0 86px; }
  .card__name { font-size: 12px; font-weight: 700; color: var(--navy); margin-bottom: 8px; }
  .contact-list { list-style: none; font-size: 8.5px; color: var(--navy); }
  .contact-list li { display: flex; align-items: center; gap: 6px; margin-bottom: 4px; }
  .contact-list svg { width: 11px; height: 11px; flex: none; }
</style>
</head>
<body>

<section class="letterhead" aria-label="Letterhead">
  <header class="letterhead__head">
    <div class="brand brand--sm"><span class="brand__mark"></span>Bright Nest Homes</div>
  </header>
  <div class="letterhead__date">Your Town, 15. January, 2016</div>

  <address class="recipient" style="font-style:normal">
    Mr Owen Hartley<br>Harbor Works Ltd<br>14 Elm Road<br>Glenvale 7257
  </address>

  <div class="letter">
    <p class="letter__salutation">Dear Mr Hartley,</p>
    <p>Fusce neque mi, consectetuer gravida, convallis ac, varius a, pede. Fusce pellentesque pretium quam. Ut luctus, justo id volutpat iaculis, est diam pulvinar sem, quis bibendum purus dui eget mauris. Sed in mauris. Ut massa. Nulla facilisi. Sed sapien ipsum, commodo at, facilisis vitae, ultrices non, enim. Curabitur molestie volutpat magna.</p>
    <p>Aliquam rhoncus volutpat mauris. Sed auctor. Donec tincidunt velit et tellus. Donec sed augue eget lacus placerat adipiscing. Ut convallis suscipit nulla. Morbi posuere ullamcorper ligula. Vivamus euismod, odio id mattis porttitor, tempor tempor.</p>
    <p>In ante. Phasellus convallis, nisl in vestibulum facilisis, lacus pede bibendum urna, dapibus pellentesque eros magna sed nibh. Etiam tortor arcu, porta nec, laoreet quis, mollis in, libero. Diam vulputate massa tempor tempus. Sed auctor.</p>
    <p class="letter__closing">Mit freundlichen Grüßen,</p>
  </div>

  <div class="signoff">
    <div class="signoff__name">Declan Ferris</div>
    <div class="signoff__role">Director</div>
    <span class="signoff__signature" role="img" aria-label="Handwritten signature of Declan Ferris"></span>
  </div>

  <footer class="letterhead__foot">
    <div class="foot__name">BRIGHT NEST HOMES</div>
    <div class="foot__contact">20 Street, Town 7274 • <b>Phone:</b> 0417 582 046 • <b>E-Mail:</b> declanferris@brightnesthomes.com.au • <b>Website:</b> www.brightnesthomes.com.au</div>
  </footer>
</section>

<div class="logo-showcase">
  <div class="brand brand--lg"><span class="brand__mark"></span>Bright Nest Homes</div>
</div>

<section class="card card--back" aria-label="Business card back">
  <div class="brand brand--md"><span class="brand__mark"></span>Bright Nest Homes</div>
</section>

<section class="card card--front" aria-label="Business card front">
  <div class="brand brand--sm"><span class="brand__mark"></span>Bright Nest Homes</div>
  <div class="card__person">
    <div class="card__name">Declan Ferris</div>
    <ul class="contact-list">
      <li>
        <svg viewBox="0 0 12 12" aria-hidden="true"><rect width="12" height="12" rx="2" fill="#f47b20"/><path d="M4 3l1.3 1.6-.7.8c.4.9 1.1 1.6 2 2l.8-.7L9 8l-.6 1C6 9 3 6 3 3.6z" fill="#fff"/></svg>
        0417 582 046
      </li>
      <li>
        <svg viewBox="0 0 12 12" aria-hidden="true"><rect width="12" height="12" rx="2" fill="#f47b20"/><rect x="2.5" y="3.5" width="7" height="5" fill="none" stroke="#fff" stroke-width=".9"/><path d="M2.5 3.5L6 6.3l3.5-2.8" fill="none" stroke="#fff" stroke-width=".9"/></svg>
        declanferris@brightnesthomes.com.au
      </li>
      <li>
        <svg viewBox="0 0 12 12" aria-hidden="true"><rect width="12" height="12" rx="2" fill="#f47b20"/><circle cx="6" cy="6" r="3.3" fill="none" stroke="#fff" stroke-width=".9"/><path d="M2.7 6h6.6M6 2.7c-1.5 1.8-1.5 4.8 0 6.6M6 2.7c1.5 1.8 1.5 4.8 0 6.6" fill="none" stroke="#fff" stroke-width=".7"/></svg>
        www.brightnesthomes.com.au
      </li>
    </ul>
  </div>
</section>

</body>
</html>
```